40% Off Colour And Hair Service Every Monday + Wedneday

A large window poster approx 1m x 1m when installed
The poster should in someway match the look of our website
corvella.net.au
please refer to our website for selection of images and choose something similar yourself
final print needs to suitable for a large format poster

.
.
.
.
.
.
.
.
.
.
.
.
.

Target Market(s)

people passing the salon

Industry/Entity Type

Hair And Beauty

Colors

Designer to choose colors to be used in the design.

Requirements
Must have
• (the offer) : 40% Off Colour And Hair Services Every Monday & Wednesday
• (image) : in keeping with our website : corvella.net.au
• Phone Number : 9381 5067
• (disclaimer - small print)
• Offer Not Available During Christmas Period. Offer
• Excludes Keratin and Hair Extensions
• 40% discount apples to full price adult services – cannot be combined with any other discount
Nice to have
• in keeping with feel of our website: corvella.net.au
• must be bold, eye catching and easily readable
• sophisticated / classy / modern feel .. nothing tacky

```html
<!DOCTYPE html>
<html lang="en">
<head>
<meta charset="utf-8">
<title>Corvella Salon &amp; Spa – 40% Off Poster</title>
<link rel="stylesheet" href="https://fonts.googleapis.com/css2?family=Roboto+Condensed:wght@300;400;700&display=swap">
<style>
  :root {
    --brand-red: #c8202f;
    --ink: #111111;
    --paper: #ffffff;
    --rule-grey: #c9c9c9;
    --fern: #2f5a3e;
    --fern-deep: #14301f;
    --teal: #11a9bd;
    --teal-deep: #0a7c8c;
    --rock: #3a4036;
    --warm: #a8765a;
    --warm-deep: #5a3a2c;
  }
  html, body {
    margin: 0;
    padding: 0;
    width: 1200px;
    height: 1200px;
    overflow: hidden;
    background: var(--paper);
  }
  .poster {
    position: relative;
    width: 1200px;
    height: 1200px;
    background: var(--paper);
    font-family: "Roboto Condensed", "Arial Narrow", sans-serif;
    color: var(--ink);
  }
  .collage {
    position: absolute;
    left: 0;
    top: 0;
  }
  .edge-stripe {
    position: absolute;
    top: 0;
    height: 1200px;
  }
  .edge-stripe--red { left: 1124px; width: 12px; background: var(--brand-red); }
  .edge-stripe--black { left: 1145px; width: 13px; background: var(--ink); }

  .offer-column {
    position: absolute;
    left: 600px;
    width: 520px;
    top: 0;
    height: 1200px;
    text-align: center;
  }
  .offer-column > * { position: absolute; left: 0; right: 0; margin: 0; }

  .brand-name {
    top: 178px;
    font-size: 112px;
    font-weight: 700;
    letter-spacing: -2px;
    line-height: 1;
    color: var(--brand-red);
  }
  .brand-rule {
    top: 288px;
    left: 25px;
    right: 19px;
    height: 1px;
    background: var(--rule-grey);
  }
  .brand-tagline {
    top: 292px;
    font-size: 31px;
    font-weight: 700;
    letter-spacing: 17px;
    padding-left: 20px;
    line-height: 1.2;
  }
  .discount {
    top: 366px;
    left: 44px;
    right: auto;
    font-size: 236px;
    font-weight: 300;
    line-height: 1;
    letter-spacing: -12px;
    white-space: nowrap;
    color: var(--brand-red);
  }
  .discount-off {
    top: 424px;
    left: 388px;
    right: auto;
    width: 144px;
    height: 72px;
    font-size: 92px;
    font-weight: 400;
    line-height: 72px;
    transform-origin: 0 0;
    transform: translate(0, 144px) rotate(-90deg);
    text-align: center;
    white-space: nowrap;
  }
  .service-line {
    top: 574px;
    font-size: 40px;
    font-weight: 700;
    line-height: 1.1;
  }
  .days-line {
    top: 620px;
    font-size: 38px;
    font-weight: 400;
    line-height: 1.1;
  }
  .call-label {
    top: 699px;
    left: 20px;
    font-size: 32px;
    font-weight: 400;
    color: var(--brand-red);
    line-height: 1.1;
  }
  .phone-number {
    top: 730px;
    font-size: 104px;
    font-weight: 700;
    line-height: 1.05;
    color: var(--brand-red);
  }
  .fine-print {
    top: 874px;
    font-size: 18.5px;
    line-height: 23px;
  }
  .fine-print p { margin: 0; }
  .fine-print p + p { margin-top: 24px; }
  .web-address {
    top: 1067px;
    font-size: 48px;
    font-weight: 300;
    line-height: 1.1;
  }
</style>
</head>
<body>
<main class="poster">
  <svg class="collage" width="567" height="1200" viewBox="0 0 567 1200">
    <defs>
      <linearGradient id="grad-portrait" x1="0" y1="0" x2="1" y2="1">
        <stop offset="0" stop-color="var(--fern-deep)"/>
        <stop offset="0.5" stop-color="var(--fern)"/>
        <stop offset="1" stop-color="#1d4029"/>
      </linearGradient>
      <linearGradient id="grad-teal" x1="0" y1="0" x2="1" y2="1">
        <stop offset="0" stop-color="var(--teal)"/>
        <stop offset="1" stop-color="var(--teal-deep)"/>
      </linearGradient>
      <linearGradient id="grad-waterfall" x1="0" y1="0" x2="1" y2="1">
        <stop offset="0" stop-color="#55636a"/>
        <stop offset="1" stop-color="var(--rock)"/>
      </linearGradient>
      <linearGradient id="grad-makeup" x1="0" y1="0" x2="1" y2="1">
        <stop offset="0" stop-color="var(--warm)"/>
        <stop offset="1" stop-color="var(--warm-deep)"/>
      </linearGradient>
    </defs>
    <polygon class="collage-photo collage-photo--portrait" role="img"
      aria-label="Photo: model with sleek swept-back hair in front of tropical leaves"
      points="0,0 567,0 567,381 344,381 344,391 250,391 250,471 0,471"
      fill="url(#grad-portrait)"/>
    <rect class="collage-photo collage-photo--groomed" role="img"
      aria-label="Photo: man with styled hair and beard in a waistcoat on a teal backdrop"
      x="252" y="391" width="315" height="411" fill="url(#grad-teal)"/>
    <rect class="collage-photo collage-photo--waterfall" role="img"
      aria-label="Photo: platinum-blonde model beside a waterfall"
      x="0" y="481" width="305" height="330" fill="url(#grad-waterfall)"/>
    <polygon class="collage-photo collage-photo--makeup" role="img"
      aria-label="Photo: stylist applying make-up to a client with auburn hair"
      points="0,811 211,811 211,802 567,802 567,812 567,1200 0,1200"
      fill="url(#grad-makeup)"/>
    <rect x="211" y="802" width="356" height="9" fill="var(--paper)"/>
  </svg>

  <div class="edge-stripe edge-stripe--red"></div>
  <div class="edge-stripe edge-stripe--black"></div>

  <section class="offer-column">
    <h1 class="brand-name">corvella</h1>
    <div class="brand-rule"></div>
    <p class="brand-tagline">salon &amp; spa</p>

    <p class="discount">40%</p>
    <p class="discount-off">OFF</p>

    <p class="service-line">Colour And Hair Services</p>
    <p class="days-line">Every Monday &amp; Wednesday</p>

    <p class="call-label">CALL US NOW</p>
    <p class="phone-number">9381 5067</p>

    <div class="fine-print">
      <p>Offer Not Available During Christmas Period.</p>
      <p>Offer Excludes Keratin and Hair Extensions<br>
      40% discount apples to full price adult services<br>
      cannot be combined with any other discount</p>
    </div>

    <p class="web-address">www.corvella.net.au</p>
  </section>
</main>
</body>
</html>
```